Zielgruppe
Die Zielgruppe besteht aus allen Privatpersonen, die eine Feier planen und auf der Suche nach individuellen, professionell gestalteten Einladungskarten für Ihre Feier sind:
Hochzeit
Geburtstag (meistens runde Geburtstage)
Mottoparty´s
Danksagung zur Gebur
Aufgabenstellung
Für das Online-Angebot www.festpost-atelier.de werden kreative Vorschläge für Einladungskarten und Danksagungskarten in verschiedenen Kategorien gesucht: Hochzeit, Geburtstag, Party, Mottoparty, Geburt und weitere Themen. Das Thema ist wählbar, da für alle Kategorien neue, frische Entwürfe benötigt werden.
Dies ist kein Wettbewerb im herkömmlichen Sinne, da es keinen einzelnen Gewinner gibt. Jeder Kartenentwurf, der für das Online Angebot ausgewählt wird, wird mit 100,00 Eur honoriert.
Voraussetzung für die Honorarzahlung ist das Einverständnis der Veröffentlichung und die Übertragung der Nutzungsrechte.

```html
<!DOCTYPE html>
<html lang="de">
<head>
<meta charset="utf-8">
<title>Hochzeitseinladung – Lene &amp; Jonas</title>
<link rel="stylesheet" href="https://fonts.googleapis.com/css2?family=Great+Vibes&family=Dancing+Script:wght@400;600&display=swap">
<style>
  :root {
    --crimson: #b2234f;
    --crimson-soft: #d46a8a;
    --ink-grey: #4f4f4f;
    --name-grey: #b9b9b9;
    --amp-grey: #e6e6e6;
    --motif-grey: #e4e4e4;
    --motif-grey-light: #f3f3f3;
    --edge: #8a8a8a;
    --paper: #ffffff;
    --canvas: #ffffff;
  }
  * { box-sizing: border-box; margin: 0; padding: 0; }
  html, body { width: 1200px; height: 920px; overflow: hidden; background: var(--canvas); }
  .canvas { position: relative; width: 1200px; height: 920px; }

  .card-sheet {
    position: absolute; left: 33px; width: 1125px;
    background: var(--paper); border: 1px solid var(--edge);
  }
  .sheet-outside { top: 33px; height: 392px; }
  .sheet-inside { top: 489px; height: 426px; }

  .fold { position: absolute; top: 0; bottom: 0; left: 561px; width: 1px; background: var(--edge); }

  .stripe-band { position: absolute; left: 0; right: 0; height: 12px; }
  .stripe-band::before, .stripe-band::after {
    content: ""; position: absolute; left: 0; right: 0; background: var(--crimson);
  }
  .stripe-band::before { top: 0; height: 3px; }
  .stripe-band::after { top: 8px; height: 2px; }
  .sheet-outside .stripe-top { top: 12px; }
  .sheet-outside .stripe-bottom { top: 375px; }
  .sheet-inside .stripe-top { top: 11px; }
  .sheet-inside .stripe-bottom { top: 377px; }

  .script { font-family: "Dancing Script", cursive; }

  .sender-line {
    position: absolute; left: 122px; top: 356px;
    font-size: 14px; color: var(--ink-grey); white-space: nowrap;
  }

  .ornament-garland {
    position: absolute; left: 612px; top: 95px; width: 473px; height: 120px;
    background: radial-gradient(ellipse at 50% 50%, var(--crimson-soft) 0%, rgba(212,106,138,.45) 45%, rgba(255,255,255,0) 75%);
  }
  .couple-names {
    position: absolute; left: 690px; top: 220px; width: 330px; height: 80px;
    font-family: "Great Vibes", cursive;
  }
  .couple-names .name {
    position: absolute; top: 14px; font-size: 40px; color: var(--name-grey);
  }
  .couple-names .name-first { left: 15px; }
  .couple-names .name-second { left: 205px; }
  .couple-names .amp {
    position: absolute; left: 124px; top: -6px; font-size: 92px; color: var(--amp-grey);
  }

  .ornament-motif {
    position: absolute; left: 12px; top: 118px; width: 195px; height: 165px;
    border-radius: 12px;
    background: linear-gradient(160deg, var(--motif-grey) 0%, var(--motif-grey-light) 100%);
    opacity: .7;
  }
  .verse {
    position: absolute; left: 92px; top: 201px;
    font-size: 16px; line-height: 24px; color: var(--ink-grey); white-space: nowrap;
  }

  .invitation { position: absolute; left: 598px; top: 52px; width: 510px; }
  .invitation-title {
    font-family: "Great Vibes", cursive; font-weight: 400;
    font-size: 42px; color: var(--crimson); line-height: 1;
  }
  .invitation-text {
    margin-top: 22px; font-size: 15px; line-height: 22px; color: var(--ink-grey); white-space: nowrap;
  }
  .event-list { list-style: none; margin-top: 22px; }
  .event-list li {
    font-size: 14px; font-weight: 600; color: var(--crimson); line-height: 32px;
  }
</style>
</head>
<body>
<div class="canvas">

  <section class="card-sheet sheet-outside" aria-label="Außenseite der Karte">
    <div class="stripe-band stripe-top"></div>
    <div class="fold"></div>
    <p class="sender-line script">Lene &amp; Jonas &nbsp;|&nbsp; Lindenweg 4 &nbsp;|&nbsp; 3000 Festhausen</p>

    <div class="ornament-garland" role="img" aria-label="Florale Ranke mit Herz und Schmetterling"></div>
    <div class="couple-names">
      <span class="amp">&amp;</span>
      <span class="name name-first">Lene</span>
      <span class="name name-second">Jonas</span>
    </div>
    <div class="stripe-band stripe-bottom"></div>
  </section>

  <section class="card-sheet sheet-inside" aria-label="Innenseite der Karte">
    <div class="stripe-band stripe-top"></div>
    <div class="fold"></div>

    <div class="ornament-motif" role="img" aria-label="Dekoratives florales Herzornament in Hellgrau"></div>
    <p class="verse script">
      Zusammen durch die Welt zu gehen ist schöner, als allein zu stehen.<br>
      Und sich darauf das Wort zu geben ist wohl das Schönste im Leben.
    </p>

    <div class="invitation">
      <h1 class="invitation-title">Wir Heiraten....</h1>
      <p class="invitation-text script">
        Lorem ipsum dolor sit amet, consetetur sadipscing elitr, sed diam nonumy<br>
        eirmod tempor invidunt ut labore et dolore magna aliquyam erat, sed diam<br>
        voluptua. At vero eos et accusam et justo duo dolores et ea rebum. Stet clita<br>
        kasd gubergren, no sea takimata sanctus est Lorem ipsum dolor sit amet.
      </p>
      <ul class="event-list script">
        <li>Standesamt:</li>
        <li>Kirchliche Trauung:</li>
        <li>Hochzeitsparty:</li>
      </ul>
    </div>
    <div class="stripe-band stripe-bottom"></div>
  </section>

</div>
</body>
</html>
```